Long Established Local Fencing (not swords) Business needs fresh Business Cards

We need fresh double sided business cards for our Fencing Construction business, we are looking for something with our new logo design added, and maybe a photo background ?
We recently had cards made from Quillmarko and we were horrified with what we got back, the quality was terrible, so am looking for high quality format for good printing company to make.
We install Steelwave, Timber paling, Aluminium Slat Screening, Picket (timber and aluminium) and most other fencing installations.
Our website is brelbanfencing.com.au should you like to learn a bit more.
We do have logo in other formats if required.
We have been in business for over 35 years and we have used this as a "motto" it is on our signage

Industry/Entity Type

Construction

Contact Information for Business Card

Open to ideas, we need 3 x different cards, one generic with no name and 2 x others each with 1 of our bosses name on each, I will put into upload files.

Colors
ec1f27
000000
606060
f5f5f5

Requirements
Must have
• Company Name and Logo
• Address
• Contact details, phone, website, email etc
• Small space to write notes when leaving card at residence
Nice to have
• Our motto "Servicing the Peninsula for over 35 years"

```html
<!DOCTYPE html>
<html lang="en">
<head>
<meta charset="utf-8">
<title>Brelban Fencing – Business Cards</title>
<link href="https://fonts.googleapis.com/css2?family=Open+Sans:wght@400;600;800&display=swap" rel="stylesheet">
<style>
  :root {
    --red: #ec1f27;
    --black: #000000;
    --grey: #606060;
    --dark: #3a3a3c;
    --paper: #f5f5f5;
    --white: #ffffff;
    --stage: #4a4a4a;
  }
  * { box-sizing: border-box; margin: 0; padding: 0; }
  html, body { width: 1200px; height: 900px; overflow: hidden; }
  body {
    background: var(--stage);
    font-family: "Open Sans", Arial, sans-serif;
    position: relative;
  }
  .card {
    position: absolute;
    width: 540px;
    height: 310px;
    border-radius: 26px;
    overflow: hidden;
  }
  /* Front */
  .card-front { left: 40px; top: 150px; }
  .card-front .photo {
    position: absolute; inset: 0;
    background: linear-gradient(180deg, #5d6066 0%, #7b7f86 35%, #4f5358 60%, #2f4a2a 78%, #3f6a32 100%);
  }
  .card-front .brand {
    position: absolute; left: 0; right: 0; top: 118px;
    text-align: center;
  }
  .brand-name {
    font-weight: 800;
    letter-spacing: 2px;
    line-height: 1.05;
    text-transform: uppercase;
  }
  .card-front .brand-name { color: var(--white); font-size: 40px; }
  .brand-dot {
    display: inline-block; width: 18px; height: 18px;
    border-radius: 50%; background: var(--red); margin-bottom: 10px;
  }
  /* Back */
  .card-back {
    left: 620px; top: 410px;
    background: linear-gradient(135deg, var(--white) 0%, var(--paper) 60%, #e9e9e9 100%);
  }
  .card-back .brand { position: absolute; left: 46px; top: 40px; }
  .card-back .brand-name { color: var(--dark); font-size: 34px; }
  .contacts {
    position: absolute; left: 46px; top: 138px;
    list-style: none; font-size: 15px; color: var(--dark); line-height: 23px;
  }
  .contacts li { display: flex; align-items: center; gap: 10px; }
  .contacts svg { width: 14px; height: 14px; fill: var(--red); flex: none; }
  .holder {
    position: absolute; right: 46px; top: 118px; text-align: right;
  }
  .holder-name { color: var(--red); font-weight: 800; font-size: 20px; text-transform: uppercase; }
  .holder-licence { color: var(--dark); font-size: 10px; text-transform: uppercase; margin-top: 2px; }
  .tab {
    position: absolute; right: 0; top: 122px; width: 16px; height: 46px;
    background: var(--red); border-radius: 6px 0 0 6px;
  }
  .band {
    position: absolute; left: 0; right: 0; top: 236px; height: 30px;
    background: var(--red); color: var(--white);
    display: flex; align-items: center; justify-content: space-between;
    padding: 0 46px 0 40px; font-size: 14px;
  }
  .band .web { display: flex; align-items: center; gap: 8px; }
  .band .web b { font-weight: 800; }
  .band svg { width: 15px; height: 15px; }
  .band .abn { font-size: 10px; }
</style>
</head>
<body>

<section class="card card-front">
  <div class="photo" role="img" aria-label="Photo of a grey corrugated steel fence with green shrubs and lawn in front"></div>
  <div class="brand">
    <span class="brand-dot"></span>
    <div class="brand-name">Brelban<br>Fencing</div>
  </div>
</section>

<section class="card card-back">
  <div class="brand">
    <div class="brand-name">Brelban<br>Fencing</div>
  </div>

  <ul class="contacts">
    <li><svg viewBox="0 0 24 24"><path d="M3 7c0-2 3-4 9-4s9 2 9 4v2h-5V7H8v2H3zM6 11h12l2 9H4z"/></svg>(02) 4000 5182</li>
    <li><svg viewBox="0 0 24 24"><path d="M7 1h10a2 2 0 0 1 2 2v18a2 2 0 0 1-2 2H7a2 2 0 0 1-2-2V3a2 2 0 0 1 2-2zm0 3v14h10V4zm5 15.5a1.2 1.2 0 1 0 0 2.4 1.2 1.2 0 0 0 0-2.4z"/></svg>0400 627 308</li>
    <li><svg viewBox="0 0 24 24"><path d="M2 5h20v14H2zm2 2v.5l8 6 8-6V7zm0 3v7h16v-7l-8 6z"/></svg>brelbanfencing@mailroo.com</li>
    <li><svg viewBox="0 0 24 24"><path d="M12 1a8 8 0 0 1 8 8c0 6-8 14-8 14S4 15 4 9a8 8 0 0 1 8-8zm0 5a3 3 0 1 0 0 6 3 3 0 0 0 0-6z"/></svg>PO Box 218, Marlow Bay NSW 2260</li>
  </ul>

  <div class="holder">
    <div class="holder-name">Darren Kellow</div>
    <div class="holder-licence">Gold Licence No. 40215C</div>
  </div>
  <div class="tab"></div>

  <div class="band">
    <span class="web">
      <svg viewBox="0 0 24 24" fill="none" stroke="#fff" stroke-width="2"><circle cx="12" cy="12" r="9"/><path d="M3 12h18M12 3c3 3 3 15 0 18M12 3c-3 3-3 15 0 18"/></svg>
      <span>www.<b>brelbanfencing</b>.com.au</span>
    </span>
    <span class="abn">ABN 12 345 67 890</span>
  </div>
</section>

</body>
</html>
```